Proposal Cover Page for logistics technology company

We need a really sharp looking cover page. Full graphics page 8 1/2 x 11 size, incorporating our logo. We are a professional technology firm with clear and crisp branding, please see our web site, logo, and brochure file for example. Modern, but professional look. Graphics should focus on technology .... not so much logistics.

Industry/Entity Type

Technical Service

Requirements
Must have
• Graphic design, great looking cover page
Nice to have
• Graphics that connects things. Yes, this is a bit abstract. Be creative. Not simple dot-to-dot, but something illustrating that.
Should not have
• No trucks, ships and planes

```html
<!DOCTYPE html>
<html lang="en">
<head>
<meta charset="utf-8">
<title>Corporate Cover Design Template</title>
<link rel="stylesheet" href="https://fonts.googleapis.com/css2?family=Barlow+Semi+Condensed:wght@500;600;700&family=Barlow:wght@400;600;700&display=swap">
<style>
  :root {
    --backdrop: #ebecee;
    --paper: #ffffff;
    --navy: #0d3a6e;
    --navy-deep: #082a55;
    --sky: #1aa3e8;
    --mist: #d6d7d9;
    --ink: #1f2022;
    --muted: #7a7d82;
  }
  * { margin: 0; padding: 0; box-sizing: border-box; }
  html, body {
    width: 1200px;
    height: 900px;
    overflow: hidden;
    background: var(--backdrop);
  }
  .canvas {
    width: 1200px;
    height: 900px;
    display: flex;
    align-items: center;
    justify-content: center;
  }
  .cover {
    position: relative;
    width: 520px;
    height: 730px;
    background: var(--paper);
    overflow: hidden;
    box-shadow: 0 6px 24px rgba(0, 0, 0, 0.12);
  }
  .cover-art {
    position: absolute;
    top: 0;
    left: 0;
    width: 520px;
    height: 730px;
  }
  .brand-name {
    position: absolute;
    top: 92px;
    right: 34px;
    font-family: "Barlow", sans-serif;
    font-weight: 700;
    font-size: 23px;
    color: var(--paper);
    letter-spacing: 0.2px;
  }
  .cover-text {
    position: absolute;
    left: 68px;
    top: 488px;
    width: 380px;
  }
  .cover-title {
    font-family: "Barlow Semi Condensed", sans-serif;
    font-weight: 700;
    font-size: 37px;
    line-height: 1.05;
    color: var(--ink);
    letter-spacing: 0.3px;
  }
  .cover-subtitle {
    font-family: "Barlow Semi Condensed", sans-serif;
    font-weight: 500;
    font-size: 33px;
    line-height: 1.15;
    color: var(--sky);
    letter-spacing: 0.6px;
  }
  .cover-summary {
    margin-top: 12px;
    font-family: "Barlow", sans-serif;
    font-weight: 400;
    font-size: 10.5px;
    line-height: 1.45;
    color: var(--muted);
    letter-spacing: 0.4px;
    width: 210px;
  }
  .cover-web {
    position: absolute;
    left: 68px;
    top: 668px;
    font-family: "Barlow", sans-serif;
    font-weight: 600;
    font-size: 10px;
    color: var(--ink);
    letter-spacing: 0.3px;
  }
</style>
</head>
<body>
  <main class="canvas">
    <article class="cover">
      <svg class="cover-art" viewBox="0 0 520 730" xmlns="http://www.w3.org/2000/svg">
        <defs>
          <radialGradient id="globe-tones" cx="0.42" cy="0.3" r="0.75">
            <stop offset="0" stop-color="#f4d9a0"/>
            <stop offset="0.12" stop-color="#8fa56a"/>
            <stop offset="0.4" stop-color="#2f5a4a"/>
            <stop offset="0.75" stop-color="#0e2a4a"/>
            <stop offset="1" stop-color="#071a33"/>
          </radialGradient>
          <linearGradient id="navy-sweep" x1="0" y1="0" x2="1" y2="1">
            <stop offset="0" stop-color="var(--navy)"/>
            <stop offset="1" stop-color="var(--navy-deep)"/>
          </linearGradient>
        </defs>
        <path class="arc-band" d="M200 410 A500 500 0 0 0 440 400" fill="none" stroke="var(--mist)" stroke-width="60"/>
        <circle class="navy-field" cx="300" cy="-80" r="470" fill="url(#navy-sweep)"/>
        <circle class="globe-ring" cx="180" cy="90" r="262" fill="none" stroke="var(--sky)" stroke-width="36"/>
        <circle class="globe-image" cx="180" cy="90" r="244" fill="url(#globe-tones)" role="img" aria-label="Photograph of Earth from space with glowing network connection lines across the continents"/>
      </svg>

      <div class="brand-name">linkora.io</div>

      <div class="cover-text">
        <h1 class="cover-title">CORPORATE COVER</h1>
        <h2 class="cover-subtitle">DESIGN TEMPLATE</h2>
        <p class="cover-summary">Lorem ipsum dolor sit amet, consectetur adipiscing elit, sed do eiusmod tempor incididunt ut labore et dolore magna aliqua.</p>
      </div>

      <div class="cover-web">www.linkora.io</div>
    </article>
  </main>
</body>
</html>
```